NovaDeck website (https://novadeck.example) re-design

Website purposed for providing general information on products we develop and offer. Products are software specific to online poker players.
Software not playful but complex technological solutions so website should look neatly and professional.
More details on the project you may find in this document:
https://files.brindlepost.example/doc/7QpR2mXz9KdLw4TsVb8NcYe3HuJf6GaOi1ZtBy0Wn5e/view#part=k.mqrt4x7zb2
Or below:
Technology: preferable bootstrap, but not critical
CrossPlatform: Desktop/Mobile
Pages:
Main (Current https://novadeck.example/)
Video, Room list, Features, Price, Contacts
Partner section (whom we work with)
Documentation and FAQ links
Login (Current https://novadeck.example/Login/Login)
SignUp/Password recovery (https://novadeck.example/Signup/Signup, https://novadeck.example/Login/RemindPassword)
Dashboard (Dashboardscreen.png)
License token (unique and assigned per customer). Need an option to copy to clipboard from Dashboard screen.
Download link for latest product version.
Subs end date to display
Manuals FAQ links
Buy and renew subscription
Notes: Group everything related to subscription into one logic block on the screen.
FAQ (https://novadeck.example/Home/FAQ).
Simple and comfortable in usage faq.
Payment screen (BuySubsScreen_1.png, BuySubsScreen_2.png, BuySubsScreen_3.png)
Notes: Combine all the steps into one screen.
Make download trial which leads to registration!
Target Market(s)
Online poker players
Number of Pages Required
5+ page

```html
<!DOCTYPE html>
<html lang="en">
<head>
<meta charset="utf-8">
<title>NovaDeck — Poker Software</title>
<link rel="stylesheet" href="https://fonts.googleapis.com/css2?family=Raleway:wght@300;400;600;700&family=Mulish:wght@400;600;700&display=swap">
<style>
:root{
  --gold:#f4a900;
  --gold-dim:#5c4610;
  --ink:#1b1b1b;
  --dark:#232323;
  --panel:#2c2c2c;
  --row:#2a2a2a;
  --text:#e8e8e8;
  --muted:#c9c9c9;
  --white:#ffffff;
}
*{box-sizing:border-box;margin:0;padding:0}
html,body{width:1200px;height:4478px;overflow:hidden}
body{background:var(--dark);font-family:"Mulish",sans-serif;color:var(--text);position:relative}
.abs{position:absolute}
section,header,footer{position:absolute;left:0;width:1200px}
.heading{font-family:"Raleway",sans-serif;font-weight:300;font-size:40px;letter-spacing:1px;text-transform:uppercase;color:var(--white);text-align:center}
.heading b{font-weight:700;color:var(--gold)}
.rule{width:64px;height:4px;background:var(--gold);border-radius:2px;margin:0 auto}
.btn{display:flex;align-items:center;justify-content:center;background:var(--gold);color:var(--ink);font-weight:700;font-size:17px;border-radius:24px;text-transform:uppercase}

/* header */
.site-header{top:0;height:87px;background:var(--ink);z-index:3}
.brand{left:88px;top:8px;width:130px;text-align:center}
.brand-dot{width:30px;height:30px;border-radius:50%;background:var(--gold);margin:0 auto 4px}
.brand-name{font-family:"Mulish",sans-serif;font-weight:400;font-size:31px;color:var(--white);line-height:36px}
.nav a{position:absolute;top:52px;font-size:17px;font-weight:600;color:var(--white);text-decoration:none;white-space:nowrap}
.nav a.active{color:var(--gold)}
.login{left:1043px;top:13px;font-size:17px;font-weight:600;color:var(--white);display:flex;align-items:center;gap:8px}
.social-dot{width:12px;height:12px;border-radius:50%;background:var(--white);top:59px}

/* hero */
.hero{top:87px;height:700px}
.hero-photo{left:0;top:0;width:1200px;height:620px;background:linear-gradient(180deg,#7b7773 0%,#8c8782 45%,#a07d57 72%,#b38a5f 100%)}
.arrow{width:46px;height:46px;border-radius:50%;background:rgba(30,30,30,.75);display:flex;align-items:center;justify-content:center;top:252px}

/* welcome */
.welcome{top:760px;height:622px}
.welcome .heading{position:absolute;top:16px;width:100%}
.welcome .rule{position:absolute;top:74px;left:568px}
.welcome p{position:absolute;top:98px;left:130px;width:940px;text-align:center;font-size:16.5px;line-height:34px;color:var(--muted)}
.video{top:330px;width:324px;height:202px;border-radius:3px;overflow:hidden}
.play{left:137px;top:76px}

/* features */
.features{top:1382px;height:548px;overflow:hidden}
.features-photo{left:360px;top:0;width:840px;height:548px;background:linear-gradient(120deg,#8a8c93 0%,#5d5a60 40%,#3a3536 70%,#7e6a5f 100%)}
.features-title{left:92px;top:90px;font-family:"Raleway",sans-serif;font-weight:300;font-size:40px;color:var(--ink)}
.features-title b{font-weight:700;color:var(--white)}
.features-rule{left:92px;top:150px;width:68px;height:4px;background:var(--ink);border-radius:2px}
.features ul{position:absolute;left:90px;top:186px;width:470px;list-style:none}
.features li{position:relative;padding-left:22px;font-size:16.5px;line-height:30px;color:var(--white);margin-bottom:10px}
.features li::before{content:"»";position:absolute;left:0;top:-2px}
.btn-white{background:var(--white);color:var(--gold)}

/* rooms */
.rooms{top:1930px;height:877px}
.rooms .heading{position:absolute;top:80px;width:100%}
.rooms .rule{position:absolute;top:142px;left:568px}
.room{left:90px;width:1020px;height:106px;background:var(--row)}
.room-badge{left:0;top:0;width:148px;height:106px}
.room-icon{left:20px;top:18px;width:70px;height:70px;border-radius:12px;background:var(--ink)}
.room-icon span{position:absolute;left:15px;top:15px;width:40px;height:40px;border-radius:50%}
.room-name{left:176px;top:18px;font-size:17px;font-weight:600;color:var(--white)}
.room-rate{left:176px;top:47px;font-size:15.5px;color:var(--muted)}
.room-stars{left:176px;top:68px;font-size:11px;color:var(--gold);letter-spacing:4px}
.room-head{left:357px;top:18px;font-size:16.5px;font-weight:700;color:var(--white)}
.room-desc{left:357px;top:46px;width:460px;font-size:15.5px;line-height:23px;color:var(--muted)}
.room .btn{left:849px;top:30px;width:151px;height:48px}

/* pricing */
.pricing{top:2807px;height:735px;background:var(--panel);overflow:hidden}
.pricing .heading{position:absolute;top:84px;width:100%;font-weight:600}
.pricing .rule{position:absolute;top:144px;left:568px}
.plan{text-align:center}
.plan-basic{left:139px;top:196px;width:275px;height:411px;background:#262626}
.plan-premium{left:783px;top:196px;width:278px;height:411px;background:#262626}
.plan-standard{left:430px;top:175px;width:340px;height:475px;background:var(--gold);border-radius:4px}
.plan-name{position:absolute;width:100%;font-size:22px;font-weight:600;color:var(--white)}
.plan-price{position:absolute;width:100%;display:flex;justify-content:center;align-items:baseline;color:var(--white);font-weight:700}
.plan-price .cur{font-size:22px}
.plan-price .num{font-size:42px}
.plan-price .per{font-size:10px;font-weight:400}
.plan-list{position:absolute;left:28px;right:28px;list-style:none}
.plan-list li{height:42px;line-height:42px;border-top:1px dashed #555;font-size:16px;color:var(--muted)}
.plan-standard .plan-list li{border-top-color:#c58a05;color:var(--white)}
.plan .btn{position:absolute;width:125px;height:44px;font-size:15px}

/* partners */
.partners{top:3542px;height:385px;background:var(--dark)}
.partners .heading{position:absolute;top:82px;width:100%}
.partners .rule{position:absolute;top:140px;left:568px}
.partner{top:200px;width:82px;height:82px;border-radius:12px;background:#3a3a3a}
.partner span{position:absolute;left:21px;top:21px;width:40px;height:40px;border-radius:50%;background:#5a5a5a}
.partner.on{background:#111}
.partner.on span{background:var(--gold)}

/* newsletter */
.newsletter{top:3927px;height:181px;background:var(--gold)}
.newsletter h2{position:absolute;left:87px;top:70px;font-family:"Raleway",sans-serif;font-weight:300;font-size:33px;color:var(--white);text-transform:uppercase}
.newsletter h2 b{font-weight:700}
.news-input{left:605px;top:66px;width:371px;height:45px;background:var(--white);font-size:13px;color:#999;padding:0 16px;line-height:45px}
.news-btn{left:976px;top:66px;width:134px;height:45px;background:var(--ink);color:var(--white);font-size:15px;font-weight:700;line-height:45px;text-align:center}

/* footer */
.site-footer{top:4108px;height:370px;background:#1d1d1d}
.foot-head{top:44px;font-size:19px;font-weight:600;color:var(--white);text-transform:uppercase}
.foot-list{top:91px;list-style:none}
.foot-list li{font-size:14px;line-height:27px;color:var(--muted)}
.foot-social{top:259px;width:42px;height:42px;border-radius:50%;background:var(--gold)}
.foot-social span{position:absolute;left:15px;top:15px;width:12px;height:12px;border-radius:50%;background:var(--white)}
.copyright{top:334px;width:100%;text-align:center;font-size:12px;color:var(--muted)}
</style>
</head>
<body>

<header class="site-header">
  <div class="abs brand"><div class="brand-dot"></div><div class="brand-name">NovaDeck</div></div>
  <nav class="nav">
    <a class="active" style="left:316px">Home</a>
    <a style="left:391px">About Us</a>
    <a style="left:492px">Features</a>
    <a style="left:590px">Price</a>
    <a style="left:656px">Documentation</a>
    <a style="left:803px">Partner</a>
    <a style="left:889px">Faq</a>
    <a style="left:946px">Contact Us</a>
  </nav>
  <div class="abs social-dot" style="left:1064px"></div>
  <div class="abs social-dot" style="left:1094px"></div>
  <div class="abs login">
    <svg width="14" height="16" viewBox="0 0 14 16"><rect x="1" y="7" width="12" height="9" rx="1" fill="#f4a900"/><path d="M4 7V4a3 3 0 0 1 6 0v3" stroke="#f4a900" stroke-width="2" fill="none"/></svg>
    Login
  </div>
</header>

<section class="hero">
  <div class="abs hero-photo" role="img" aria-label="Desk scene with a monitor showing an online poker table, a wall clock and a coffee mug"></div>
  <svg class="abs" style="left:0;top:440px" width="1200" height="260" viewBox="0 0 1200 260">
    <path d="M0 200 C250 175 420 90 640 90 C860 90 1020 140 1200 220 L1200 260 L0 260 Z" fill="#232323"/>
    <path d="M0 212 C260 190 430 105 640 100 C860 96 1030 150 1200 260 L1200 225 C1030 125 860 82 640 86 C420 92 250 180 0 196 Z" fill="#f4a900"/>
    <path d="M700 70 C900 60 1060 110 1200 190 L1200 150 C1060 80 900 48 700 70 Z" fill="#f4a900"/>
  </svg>
  <div class="abs arrow" style="left:41px"><svg width="12" height="18" viewBox="0 0 12 18"><path d="M9 2 2 9l7 7" stroke="#f4a900" stroke-width="2.5" fill="none"/></svg></div>
  <div class="abs arrow" style="left:1111px"><svg width="12" height="18" viewBox="0 0 12 18"><path d="M3 2l7 7-7 7" stroke="#f4a900" stroke-width="2.5" fill="none"/></svg></div>
</section>

<section class="welcome">
  <h1 class="heading">Welcome to <b>NovaDeck</b></h1>
  <div class="rule"></div>
  <p>Lorem ipsum dolor sit amet, consectetur adipiscing elit, sed do eiusmod tempor incididunt ut labore et dolore magna aliqua. Ut enim ad minim veniam, quis nostrud exercitation ullamco laboris nisi ut aliquip ex ea commodo consequat. Duis aute irure dolor in reprehenderit in voluptate velit esse cillum dolore eu fugiat nulla pariatur. Excepteur sint occaecat cupidatat non dent, sunt in culpa qui officia deserunt mollit anim id est laborum</p>
  <div class="abs btn" style="left:518px;top:249px;width:164px;height:45px">Read More</div>

  <div class="abs video" style="left:90px;background:linear-gradient(135deg,#3a3a3a,#555 60%,#2a2a2a)" role="img" aria-label="Video preview of the poker club setup screen">
    <svg class="abs play" width="50" height="50" viewBox="0 0 50 50"><circle cx="25" cy="25" r="23" fill="#1f1f1f" stroke="#fff" stroke-width="2"/><path d="M20 15l14 10-14 10z" fill="#fff"/></svg>
  </div>
  <div class="abs video" style="left:438px;background:linear-gradient(135deg,#f0f0f0,#d9dcc4 60%,#e6e6e6)" role="img" aria-label="Video preview of the tracker configuration guide">
    <svg class="abs play" width="50" height="50" viewBox="0 0 50 50"><circle cx="25" cy="25" r="23" fill="#1f1f1f" stroke="#fff" stroke-width="2"/><path d="M20 15l14 10-14 10z" fill="#fff"/></svg>
  </div>
  <div class="abs video" style="left:786px;background:linear-gradient(135deg,#e8ecf2,#d6dbe3 60%,#eceff3)" role="img" aria-label="Video preview of the software settings window">
    <svg class="abs play" width="50" height="50" viewBox="0 0 50 50"><circle cx="25" cy="25" r="23" fill="#1f1f1f" stroke="#fff" stroke-width="2"/><path d="M20 15l14 10-14 10z" fill="#fff"/></svg>
  </div>
</section>

<section class="features">
  <div class="abs features-photo" role="img" aria-label="Person on a sofa holding a tablet with a poker lobby on screen"></div>
  <svg class="abs" style="left:0;top:0" width="660" height="548" viewBox="0 0 660 548"><polygon points="0,0 374,0 645,278 374,548 0,548" fill="#f4a900"/></svg>
  <h2 class="abs features-title">Our <b>Features</b></h2>
  <div class="abs features-rule"></div>
  <ul>
    <li>Lorem ipsum dolor sit amet, consectetur adipiscing elit, sed do eiusmod tempor incididunt</li>
    <li>Lorem ipsum dolor sit amet, consectetur adipiscing elit, sed do eiusmod tempor incididunt</li>
    <li>Lorem ipsum dolor sit amet, consectetur adipiscing elit, sed do eiusmod tempor incididunt</li>
  </ul>
  <div class="abs btn btn-white" style="left:94px;top:414px;width:165px;height:44px">Read More</div>
</section>

<section class="rooms">
  <h2 class="heading">Room <b>List</b></h2>
  <div class="rule"></div>

  <div class="abs room" style="top:181px">
    <svg class="abs room-badge" viewBox="0 0 148 106"><polygon points="0,0 100,0 148,53 100,106 0,106" fill="#f4a900"/></svg>
    <div class="abs room-icon"><span style="background:#c0282d"></span></div>
    <div class="abs room-name">CrimsonKitePoker</div><div class="abs room-rate">Editors rating</div><div class="abs room-stars">★★★★★</div>
    <div class="abs room-head">Lorem ipsum dolor sit amet, consectetur</div>
    <div class="abs room-desc">Sed ut perspiciatis unde omnis iste natus error sit voluptatem accusantium doloremque laudantium</div>
    <div class="abs btn">Read More</div>
  </div>
  <div class="abs room" style="top:306px">
    <svg class="abs room-badge" viewBox="0 0 148 106"><polygon points="0,0 100,0 148,53 100,106 0,106" fill="#f4a900"/></svg>
    <div class="abs room-icon" style="background:#2fc6b0"><span style="background:#fff"></span></div>
    <div class="abs room-name">TablePeak</div><div class="abs room-rate">Editors rating</div><div class="abs room-stars">★★★★★</div>
    <div class="abs room-head">Lorem ipsum dolor sit amet, consectetur</div>
    <div class="abs room-desc">Sed ut perspiciatis unde omnis iste natus error sit voluptatem accusantium doloremque laudantium</div>
    <div class="abs btn">Read More</div>
  </div>
  <div class="abs room" style="top:431px">
    <svg class="abs room-badge" viewBox="0 0 148 106"><polygon points="0,0 100,0 148,53 100,106 0,106" fill="#f4a900"/></svg>
    <div class="abs room-icon"><span style="background:#d99a2b"></span></div>
    <div class="abs room-name">OpenFlop</div><div class="abs room-rate">Editors rating</div><div class="abs room-stars">★★★★★</div>
    <div class="abs room-head">Lorem ipsum dolor sit amet, consectetur</div>
    <div class="abs room-desc">Sed ut perspiciatis unde omnis iste natus error sit voluptatem accusantium doloremque laudantium</div>
    <div class="abs btn">Read More</div>
  </div>
  <div class="abs room" style="top:557px">
    <svg class="abs room-badge" viewBox="0 0 148 106"><polygon points="0,0 100,0 148,53 100,106 0,106" fill="#f4a900"/></svg>
    <div class="abs room-icon" style="background:#f7b733"><span style="background:#fff"></span></div>
    <div class="abs room-name">FeltCircle</div><div class="abs room-rate">Editors rating</div><div class="abs room-stars">★★★★★</div>
    <div class="abs room-head">Lorem ipsum dolor sit amet, consectetur</div>
    <div class="abs room-desc">Sed ut perspiciatis unde omnis iste natus error sit voluptatem accusantium doloremque laudantium</div>
    <div class="abs btn">Read More</div>
  </div>
  <div class="abs room" style="top:682px">
    <svg class="abs room-badge" viewBox="0 0 148 106"><polygon points="0,0 100,0 148,53 100,106 0,106" fill="#f4a900"/></svg>
    <div class="abs room-icon"><span style="background:#2a8fd6"></span></div>
    <div class="abs room-name">RiverStack</div><div class="abs room-rate">Editors rating</div><div class="abs room-stars">★★★★★</div>
    <div class="abs room-head">Lorem ipsum dolor sit amet, consectetur</div>
    <div class="abs room-desc">Sed ut perspiciatis unde omnis iste natus error sit voluptatem accusantium doloremque laudantium</div>
    <div class="abs btn">Read More</div>
  </div>
</section>

<section class="pricing">
  <svg class="abs" style="left:0;top:0" width="1200" height="735" viewBox="0 0 1200 735">
    <polygon points="0,0 40,0 130,280 0,720" fill="#5c4610"/>
    <polygon points="1200,0 1160,0 1070,280 1200,720" fill="#5c4610"/>
  </svg>
  <h2 class="heading">Pricing</h2>
  <div class="rule"></div>

  <div class="abs plan plan-basic">
    <div class="plan-name" style="top:44px">Basic</div>
    <div class="plan-price" style="top:84px"><span class="cur">$</span><span class="num">65</span><span class="per">/Per Month</span></div>
    <ul class="plan-list" style="top:160px"><li>Lorem ipsum</li><li>Lorem ipsum</li><li>Lorem ipsum</li><li>Lorem ipsum</li></ul>
    <div class="btn" style="left:75px;top:350px">Join Now</div>
  </div>
  <div class="abs plan plan-standard">
    <div class="plan-name" style="top:42px">Standard</div>
    <div class="plan-price" style="top:98px"><span class="cur">$</span><span class="num">95</span><span class="per">/Per Month</span></div>
    <ul class="plan-list" style="top:181px"><li>Lorem ipsum</li><li>Lorem ipsum</li><li>Lorem ipsum</li><li>Lorem ipsum</li></ul>
    <div class="btn" style="left:108px;top:390px;background:#fff;color:#f4a900">Join Now</div>
  </div>
  <div class="abs plan plan-premium">
    <div class="plan-name" style="top:44px">Premium</div>
    <div class="plan-price" style="top:84px"><span class="cur">$</span><span class="num">165</span><span class="per">/Per Month</span></div>
    <ul class="plan-list" style="top:160px"><li>Lorem ipsum</li><li>Lorem ipsum</li><li>Lorem ipsum</li><li>Lorem ipsum</li></ul>
    <div class="btn" style="left:76px;top:350px">Join Now</div>
  </div>
</section>

<section class="partners">
  <h2 class="heading">Our <b>Partners</b></h2>
  <div class="rule"></div>
  <svg class="abs" style="left:132px;top:228px" width="16" height="26" viewBox="0 0 16 26"><path d="M13 2 3 13l10 11" stroke="#f4a900" stroke-width="3" fill="none"/></svg>
  <div class="abs partner" style="left:209px"><span></span></div>
  <div class="abs partner" style="left:348px"><span></span></div>
  <div class="abs partner" style="left:489px"><span></span></div>
  <div class="abs partner on" style="left:628px"><span></span></div>
  <div class="abs partner" style="left:769px"><span></span></div>
  <div class="abs partner" style="left:908px"><span></span></div>
  <svg class="abs" style="left:1052px;top:228px" width="16" height="26" viewBox="0 0 16 26"><path d="M3 2l10 11-10 11" stroke="#f4a900" stroke-width="3" fill="none"/></svg>
</section>

<section class="newsletter">
  <h2>Subscribe <b>Our Newsletter</b></h2>
  <div class="abs news-input">Enter Your Email Id</div>
  <div class="abs news-btn">SUBSCRIBE</div>
</section>

<footer class="site-footer">
  <div class="abs foot-head" style="left:92px">Quick Links</div>
  <ul class="abs foot-list" style="left:92px"><li>Home</li><li>About Us</li><li>Features</li><li>Price</li></ul>
  <ul class="abs foot-list" style="left:374px"><li>Documentation</li><li>Partner</li><li>Faq</li><li>Contact Us</li></ul>
  <div class="abs foot-head" style="left:616px">Contact Us</div>
  <ul class="abs foot-list" style="left:616px"><li>Lorem ipsum dolor sit amet, consectetur</li><li>adipiscing elit, sed do eiusmod</li><li>765-555-0142</li><li>info@novadeck.example</li></ul>
  <div class="abs foot-head" style="left:988px">Legal</div>
  <ul class="abs foot-list" style="left:988px;top:89px"><li>Privacy Policy</li><li>Terms &amp; Conditions</li></ul>
  <div class="abs foot-social" style="left:555px"><span></span></div>
  <div class="abs foot-social" style="left:603px"><span></span></div>
  <div class="abs copyright">© Copyrights 2019.The Company Name All Rights Reserved</div>
</footer>

</body>
</html>
```